catering postcard

We need a postcard that lets offices know that we cater and can deliver our delicious food to their office/meeting/event.

We are a mom and pop, super busy, well-loved Italian restaurant.
(check us out at marcostrattoriaweb.com)

The final design should communicate delicious food, brought to your place of work. It arrives on time and is hot and ready to be devoured.

We'd like to see bright colors and a huge impact on our lunch time catering sales.

Industry/Entity Type

Catering

```html
<!DOCTYPE html>
<html lang="en">
<head>
<meta charset="utf-8">
<title>Marco's Trattoria – Catering Postcard</title>
<link href="https://fonts.googleapis.com/css2?family=Playfair+Display:wght@400;700&family=Libre+Baskerville:wght@400;700&family=Oswald:wght@300;400&family=Cookie&display=swap" rel="stylesheet">
<style>
  :root{
    --backdrop:#3b3b3b;
    --teal:#17a1a4;
    --teal-dark:#0b7478;
    --yellow:#f4c21c;
    --yellow-deep:#e9ad10;
    --green:#2a8a3e;
    --red:#b3262a;
    --white:#ffffff;
    --ink:#222222;
    --ring:#c9cdd1;
  }
  *{margin:0;padding:0;box-sizing:border-box}
  html,body{width:792px;height:1200px;overflow:hidden;background:var(--backdrop)}
  .canvas{position:relative;width:792px;height:1200px}
  .card{position:absolute;overflow:hidden;box-shadow:0 4px 14px rgba(0,0,0,.45)}
  .card-front{left:59px;top:43px;width:684px;height:529px;background:var(--yellow)}
  .card-back{left:59px;top:619px;width:688px;height:533px;background:var(--white)}
  .shapes{position:absolute;left:0;top:0}
  .photo{position:absolute}
  .hero-photo{left:0;top:0;width:684px;height:300px;
    background:linear-gradient(100deg,#e9e9ec 0%,#d9d6d6 35%,#d9735a 60%,#c9482e 78%,#b86a3a 100%)}
  .round-photo{border-radius:50%;border:7px solid var(--ring);box-shadow:0 3px 8px rgba(0,0,0,.35)}
  .photo-pasta{left:13px;top:279px;width:216px;height:216px;
    background:radial-gradient(circle at 50% 45%,#e58a3c 0%,#d0602a 40%,#f3ece8 72%,#ffffff 100%)}
  .photo-caprese{left:286px;top:191px;width:142px;height:142px;
    background:radial-gradient(circle at 45% 45%,#f4f1ea 0%,#e44a33 45%,#3e8a3a 70%,#f6f6f6 100%)}
  .photo-penne{left:175px;top:338px;width:132px;height:132px;
    background:radial-gradient(circle at 50% 60%,#d9b45a 0%,#6fa03a 50%,#f5f5f5 85%)}
  .brand{position:absolute;left:22px;top:38px;font-family:'Playfair Display',serif}
  .brand-name{display:block;font-size:34px;font-weight:700;color:var(--green);line-height:1}
  .brand-tagline{display:block;margin-top:8px;padding-top:4px;border-top:2px solid var(--green);
    font-family:'Cookie',cursive;font-size:19px;color:var(--red)}
  .headline{position:absolute;color:var(--white);font-family:'Playfair Display',serif;font-weight:400;
    transform-origin:left top;line-height:1;white-space:nowrap}
  .headline-1{left:246px;top:282px;font-size:74px;transform:scaleX(.78)}
  .headline-2{left:391px;top:347px;font-size:46px;transform:scaleX(.8)}
  .headline-3{left:467px;top:398px;font-size:100px;transform:scaleX(.78)}
  .copy{position:absolute;left:23px;color:var(--white);font-family:'Libre Baskerville',serif;
    font-size:13.2px;line-height:20.5px}
  .copy-about{top:42px;width:310px}
  .copy-catering{top:182px;width:255px}
  .signoff{position:absolute;left:23px;top:146px;font-family:'Cookie',cursive;font-size:28px;color:var(--yellow)}
  .contact{position:absolute;left:23px;font-family:'Oswald',sans-serif;font-weight:400;font-size:15px;
    color:var(--ink);line-height:23px}
  .contact-address{top:411px;padding-left:18px}
  .contact-phone{top:490px;padding-left:18px}
  .contact svg{position:absolute;left:0;top:5px}
  .social{position:absolute;top:497px;width:15px;height:15px;background:var(--teal);border-radius:3px}
  .social-1{left:266px}.social-2{left:295px}
  .stamp-box{position:absolute;left:596px;top:96px;width:58px;height:67px;border:1.5px solid var(--ink)}
  .address-line{position:absolute;left:481px;width:176px;height:1.5px;background:var(--ink)}
</style>
</head>
<body>
<main class="canvas">

  <section class="card card-front">
    <div class="photo hero-photo" role="img" aria-label="Close-up photo of tomato and basil bruschetta on a plate"></div>
    <svg class="shapes" width="684" height="529" viewBox="0 0 684 529" aria-hidden="true">
      <polygon points="0,330 684,300 684,529 0,529" fill="var(--yellow)"/>
      <polygon points="28,242 684,284 684,420 590,529 470,529 0,392" fill="var(--teal)"/>
      <polygon points="590,529 684,300 684,420 640,529" fill="var(--teal-dark)"/>
      <polygon points="0,300 28,242 0,392" fill="var(--yellow-deep)"/>
    </svg>
    <div class="photo round-photo photo-pasta" role="img" aria-label="Photo of a spaghetti nest with tomato sauce, basil and cherry tomatoes"></div>
    <div class="brand">
      <span class="brand-name">Marco's Trattoria</span>
      <span class="brand-tagline">Pizza, Pasta &amp; Caffè</span>
    </div>
    <h1>
      <span class="headline headline-1">Experience</span>
      <span class="headline headline-2">the taste of</span>
      <span class="headline headline-3">Italy</span>
    </h1>
  </section>

  <section class="card card-back">
    <svg class="shapes" width="688" height="533" viewBox="0 0 688 533" aria-hidden="true">
      <rect x="0" y="0" width="354" height="533" fill="var(--yellow)"/>
      <polygon points="0,16 354,22 354,262 0,328" fill="var(--teal)"/>
      <polygon points="354,22 382,12 382,255 354,262" fill="var(--teal-dark)"/>
    </svg>
    <p class="copy copy-about">Here at Marco's, we manage our menu closely to provide our customers with quality and delicious meals. Our daily specials reflect the seasons and availability of fresh local and regional produce."</p>
    <p class="signoff">Buon Appetito !</p>
    <p class="copy copy-catering">Offices, weddings, receptions, parties. From large to small, we cater it all. We ask that you place your catering order at least 12 hours prior to your event. We bring it to you on time and is hot and ready to be devoured.</p>
    <div class="photo round-photo photo-caprese" role="img" aria-label="Photo of caprese salad with tomato, mozzarella and basil"></div>
    <div class="photo round-photo photo-penne" role="img" aria-label="Photo of penne pasta with pesto and basil"></div>
    <address class="contact contact-address">
      <svg width="11" height="15" viewBox="0 0 11 15" aria-hidden="true"><path d="M5.5 0C2.5 0 0 2.4 0 5.4 0 9.3 5.5 15 5.5 15S11 9.3 11 5.4C11 2.4 8.5 0 5.5 0zm0 7.6a2.2 2.2 0 1 1 0-4.4 2.2 2.2 0 0 1 0 4.4z" fill="var(--ink)"/></svg>
      Marco's Trattoria<br>48 Orchard Bend Road<br>Millbrook, Alabama 36054
    </address>
    <p class="contact contact-phone">
      <svg width="13" height="13" viewBox="0 0 24 24" aria-hidden="true"><path d="M6.6 10.8a15.1 15.1 0 0 0 6.6 6.6l2.2-2.2c.3-.3.7-.4 1-.2 1.1.4 2.3.6 3.6.6.6 0 1 .4 1 1V20c0 .6-.4 1-1 1A17 17 0 0 1 3 4c0-.6.4-1 1-1h3.5c.6 0 1 .4 1 1 0 1.3.2 2.5.6 3.6.1.3 0 .7-.2 1z" fill="var(--ink)"/></svg>
      (205) 555-0182
    </p>
    <span class="social social-1" aria-hidden="true"></span>
    <span class="social social-2" aria-hidden="true"></span>
    <div class="stamp-box" aria-hidden="true"></div>
    <span class="address-line" style="top:293px"></span>
    <span class="address-line" style="top:320px"></span>
    <span class="address-line" style="top:346px"></span>
  </section>

</main>
</body>
</html>
```